Pitch deck for fundraising for a timber drying business

We have the basic content in a powerpoint but need someone to take that and make an attractive and engaging document for a reader who may see hundreds of these a week so visual impact is key.
We are launching a timber drying business in Australia using an exclusive line of kilns not otherwise available in Australia.
Designs should focus on natural tones and connections with forests and timber, probably with a green (colour) focus.
Updates

Sick

Target Market(s)

investors, wealthyindividuals

Colors

Designer to choose colors to be used in the design.

Requirements
Nice to have
• Design in Canva or similar

```html
<!DOCTYPE html>
<html lang="en">
<head>
<meta charset="utf-8">
<title>Grainline Ventures – Pitch Deck</title>
<link href="https://fonts.googleapis.com/css2?family=Signika:wght@400;600;700&family=Open+Sans:wght@400;600;700&display=swap" rel="stylesheet">
<style>
:root{
  --green:#8c9b0c;
  --lime:#b8c412;
  --brown:#7b5b1c;
  --brown-dark:#3d2b10;
  --tan:#d9c28d;
  --cream:#efe9d6;
  --ink:#333;
  --grey:#9a9a9a;
  --page:#f3f3f1;
}
*{box-sizing:border-box;margin:0;padding:0}
html,body{width:764px;height:1200px;overflow:hidden}
body{position:relative;background:var(--page);font-family:"Open Sans",sans-serif;color:var(--ink)}
.hero{position:absolute;left:0;top:0;width:764px;height:330px;background:linear-gradient(160deg,#e4ddd0 0%,#c9c4bb 45%,#b8b5ae 70%,#f3f3f1 100%)}
.hero-title{position:absolute;left:25px;top:118px;font-family:"Signika",sans-serif;font-weight:700;font-size:38px;color:var(--green);letter-spacing:-.5px}
.hero-title span{font-size:14px;font-weight:400;color:#333;letter-spacing:0;margin-left:6px}
.cover{position:absolute;left:353px;top:48px;width:311px;height:182px;background:radial-gradient(ellipse at 50% 40%,#6a4a2c,#3a2716 80%);display:flex;flex-direction:column;align-items:center;justify-content:center;color:#fff;font-family:"Signika",sans-serif}
.cover b{font-size:17px;font-weight:600;letter-spacing:.5px}
.cover i{font-style:normal;font-size:16px;font-weight:400}
.slide{position:absolute;width:245px;height:138px;background:#fff;overflow:hidden;box-shadow:0 1px 3px rgba(0,0,0,.12)}
.bar{position:absolute;left:0;top:0;width:100%;height:18px;background:var(--green);color:#fff;font-family:"Signika",sans-serif;font-weight:600;font-size:10.5px;text-align:center;line-height:18px}
.tiny{font-size:3.4px;line-height:1.35;color:#444}
.small{font-size:4.3px;line-height:1.35;color:#333}
.abs{position:absolute}
.ph{position:absolute}
.pill{position:absolute;border-radius:8px;text-align:center;color:#fff;font-weight:700;font-size:4.2px}
.num{position:absolute;font-family:"Signika",sans-serif;font-size:5px;color:#555}
.bignum{position:absolute;font-family:"Signika",sans-serif;font-size:20px;font-weight:600;color:#bbb}
.row{display:flex;align-items:center}
table{border-collapse:collapse;width:100%}
td{font-size:3.2px;padding:1.6px 2px;border-bottom:1px solid #fff;vertical-align:middle}
</style>
</head>
<body>

<div class="hero" role="img" aria-label="Photograph of friends with raised hands at sunset"></div>
<div class="hero-title">Presentation<span>Deck</span></div>
<div class="cover" role="img" aria-label="Cover slide over dark weathered wood grain">
  <b>GRAINLINE VENTURES</b><i>Pitch Deck</i>
</div>

<!-- Row 1 -->
<div class="slide" style="left:6px;top:323px">
  <div class="ph" style="inset:0;background:linear-gradient(135deg,#b08a3e,#d9b866 45%,#8c6a2c)" role="img" aria-label="Weathered timber boards with climbing ivy"></div>
  <div class="abs" style="left:60px;top:40px;width:160px;text-align:center;font-family:'Signika',sans-serif;color:#7b5b1c">
    <div style="font-size:15px;font-weight:600">GRAINLINE VENTURES</div>
    <div style="font-size:16px;color:#9c7e4a">Pitch Deck</div>
  </div>
</div>

<div class="slide" style="left:260px;top:323px;background:var(--green)">
  <div class="ph" style="left:38px;top:36px;width:170px;height:58px;border-radius:6px;background:linear-gradient(#e9a867,#c97d3f);border:2px solid #5a3514" role="img" aria-label="Illustrated wooden signboard"></div>
  <div class="abs" style="left:38px;top:48px;width:170px;text-align:center;font-family:'Signika',sans-serif;color:#3d2310">
    <div style="font-size:13px;font-weight:700">GRAINLINE VENTURES</div>
    <div style="font-size:10px;font-weight:700">Pitch Deck</div>
  </div>
</div>

<div class="slide" style="left:513px;top:323px">
  <div class="ph" style="left:135px;top:0;width:110px;height:138px;background:linear-gradient(90deg,#c9a36a,#e6cfa2,#b88d50)" role="img" aria-label="Stacked hardwood boards"></div>
  <div class="abs" style="left:11px;top:9px;width:210px;height:120px;border-radius:8px;background:rgba(140,155,12,.93)"></div>
  <div class="abs" style="left:115px;top:18px;font-family:'Signika',sans-serif;color:#fff;font-size:11px;font-weight:600">INTRODUCTION</div>
  <div class="abs" style="left:18px;top:30px;width:82px;color:#fff">
    <div class="row" style="margin-bottom:4px"><b style="font-size:10px;width:10px">1</b><span class="tiny" style="color:#fff">GVI holds exclusive access to a proven vacuum drying technology in use since 1980.</span></div>
    <div class="row" style="margin-bottom:4px"><b style="font-size:10px;width:10px">2</b><span class="tiny" style="color:#fff">GVI will use it to build a hardwood drying business for Sydney and Brisbane.</span></div>
    <div class="row" style="margin-bottom:4px"><b style="font-size:10px;width:10px">3</b><span class="tiny" style="color:#fff">Hardwood stair tread timber has a gross margin of $XXX/m3.</span></div>
    <div class="row"><b style="font-size:10px;width:10px">4</b><span class="tiny" style="color:#fff">GVI sells directly to installers, retaining most of the margin.</span></div>
  </div>
  <div class="abs" style="left:116px;top:45px;width:92px;color:#fff">
    <div class="row" style="margin-bottom:6px"><b style="font-size:10px;width:11px">5</b><span class="tiny" style="color:#fff">A long term cash cow with a simple model in a stagnant industry.</span></div>
    <div class="row" style="margin-bottom:6px"><b style="font-size:10px;width:11px">6</b><span class="tiny" style="color:#fff">Kilns are modular, inexpensive and return about 500% per annum.</span></div>
    <div class="row"><b style="font-size:10px;width:11px">7</b><span class="tiny" style="color:#fff">The Australian hardwood industry is worth $7bn, with large export value.</span></div>
  </div>
</div>

<!-- Row 2 -->
<div class="slide" style="left:6px;top:467px">
  <div class="bar">Business model</div>
  <div class="abs small" style="left:50px;top:26px;width:150px;text-align:center">We are using established technology to disrupt the existing timber supply chain with a simple 4 step business model</div>
  <div class="abs" style="left:26px;top:45px;display:flex;gap:7px">
    <div style="width:43px;height:68px;background:var(--green);position:relative">
      <div class="ph" style="left:3px;top:3px;width:37px;height:28px;background:#8a5a36" role="img" aria-label="Rough sawn timber stack"></div>
      <div class="abs tiny" style="left:2px;top:38px;width:39px;text-align:center;color:#fff">Buy cut timber from sawmills</div>
      <div class="pill" style="left:5px;top:55px;width:33px;height:8px;line-height:8px;background:var(--brown)">$XXX m3</div>
    </div>
    <div style="width:43px;height:68px;background:var(--green);position:relative">
      <div class="ph" style="left:3px;top:3px;width:37px;height:28px;background:#9d8e78" role="img" aria-label="Timber loaded in kiln"></div>
      <div class="abs tiny" style="left:2px;top:40px;width:39px;text-align:center;color:#fff">Dry it in our kilns</div>
      <div class="pill" style="left:5px;top:55px;width:33px;height:8px;line-height:8px;background:var(--brown)">$XXXm3</div>
    </div>
    <div style="width:43px;height:68px;background:var(--green);position:relative">
      <div class="ph" style="left:3px;top:3px;width:37px;height:28px;background:#7c8a8c" role="img" aria-label="Dressing machinery"></div>
      <div class="abs tiny" style="left:2px;top:40px;width:39px;text-align:center;color:#fff">Dress and deliver</div>
      <div class="pill" style="left:5px;top:55px;width:33px;height:8px;line-height:8px;background:var(--brown)">$XXXm3</div>
    </div>
    <div style="width:43px;height:68px;background:var(--green);position:relative">
      <div class="ph" style="left:3px;top:3px;width:37px;height:28px;background:#f4f1ec" role="img" aria-label="Finished stair tread"></div>
      <div class="abs tiny" style="left:2px;top:38px;width:39px;text-align:center;color:#fff">Sell dried stair treads to installers</div>
      <div class="pill" style="left:5px;top:55px;width:33px;height:8px;line-height:8px;background:var(--brown)">$XXXm3</div>
    </div>
  </div>
  <div class="pill" style="left:93px;top:118px;width:60px;height:14px;padding-top:2px;background:var(--lime);line-height:1.3">~ $XXXm3<br>Net profit</div>
</div>

<div class="slide" style="left:260px;top:467px">
  <div class="bar">Why stair treads</div>
  <div class="ph" style="left:0;top:18px;width:76px;height:120px;background:linear-gradient(180deg,#a77a4c,#d1ad80,#8b5e36,#c99c6c)" role="img" aria-label="Stacked timber ends"></div>
  <div class="abs" style="left:64px;top:28px;width:170px">
    <div class="row small" style="height:15px"><span style="width:18px;color:#fff">1</span><b>XX%</b>&nbsp;margin</div>
    <div class="row small" style="height:15px"><span style="width:18px;color:#fff">2</span>High absolute $ returns – <b>&nbsp;~$XXXm3 profit</b></div>
    <div class="row small" style="height:15px"><span style="width:18px;color:#fff">3</span>Standardised product allowing optimisation of production processes</div>
    <div class="row small" style="height:19px"><span style="width:18px;color:#fff">4</span><span>Large market – over <b>65 potential clients indicated</b> interest in purchasing in Sydney alone</span></div>
    <div class="row small" style="height:19px"><span style="width:18px;color:#fff">5</span><span>Installers looking for alternatives – <b>~30% of Stonefield products out of specification resulting in no installer profit</b> on those jobs</span></div>
    <div class="row small" style="height:15px"><span style="width:18px;color:#fff">6</span><span>Significant drying time advantage over competitors: <b>1 week v 7-8 months</b></span></div>
  </div>
</div>

<div class="slide" style="left:513px;top:467px">
  <div class="bar" style="height:3px;left:112px;width:20px;background:var(--brown)"></div>
  <div class="bar" style="height:3px;top:0"></div>
  <div class="bignum" style="left:20px;top:30px">1</div>
  <div class="abs tiny" style="left:22px;top:28px;width:100px">The total value of the Australian timber market is $23.9bn, with hardwood accounting for $7bn. Harvest volumes grew strongly, with a 13% rise in price in 2017.</div>
  <div class="bignum" style="left:20px;top:62px">2</div>
  <div class="abs tiny" style="left:22px;top:64px;width:100px">The hardwood industry however is massively under developed, with most logs exported with no value adding.</div>
  <div class="bignum" style="left:20px;top:92px">3</div>
  <div class="abs tiny" style="left:22px;top:94px;width:100px">In NSW logs are sourced from State Forests or private forests. GVI will begin with State Forests, then add private growers to secure supply and mitigate risk.</div>
  <div class="bignum" style="left:141px;top:30px">4</div>
  <div class="abs tiny" style="left:149px;top:28px;width:86px">Sawn hardwood volume in 2018 was 700,000m3. With 10 kilns we would dry less than 1% of it.</div>
  <div class="bignum" style="left:141px;top:62px">5</div>
  <div class="abs tiny" style="left:149px;top:60px;width:86px">Market research contacted 98 installers, joineries and manufacturers. Installers pay $XXX to $XXXXm3, wholesalers pay about $XXXXm3.</div>
  <div class="bignum" style="left:141px;top:100px">6</div>
  <div class="abs tiny" style="left:149px;top:110px;width:86px">Include timber data on stair tread market</div>
</div>

<!-- Row 3 -->
<div class="slide" style="left:6px;top:614px">
  <div class="bar">Comparison of drying techniques</div>
  <div class="abs" style="left:122px;top:18px;width:123px;height:120px;background:var(--brown)"></div>
  <div class="abs small" style="left:40px;top:30px;font-size:5.5px;font-weight:600">Competitors</div>
  <div class="abs tiny" style="left:13px;top:42px;width:95px">Green cut timber is left to air dry from 40% moisture to 20-25%, taking 6-12 months depending on thickness and weather</div>
  <div class="ph" style="left:12px;top:58px;width:46px;height:30px;background:#8d6a52" role="img" aria-label="Air drying timber stacks"></div>
  <div class="ph" style="left:60px;top:58px;width:46px;height:30px;background:#b7c3c7" role="img" aria-label="Conventional kiln room"></div>
  <div class="abs tiny" style="left:13px;top:96px;width:95px">Air dried timber is loaded into an insulated room with multiple fans and a heat source.</div>
  <div class="abs tiny" style="left:13px;top:110px">Drying takes 2-6 weeks for 50mm timber.</div>
  <div class="pill" style="left:28px;top:119px;width:67px;height:9px;line-height:9px;background:var(--brown)">Total time 7-14 months</div>
  <div class="abs" style="left:113px;top:62px;width:20px;height:20px;border-radius:50%;background:var(--lime);color:#fff;font-size:7px;font-weight:700;text-align:center;line-height:20px">VS.</div>
  <div class="abs small" style="left:160px;top:30px;color:#fff;font-size:5.5px;font-weight:600">Grainline Ventures</div>
  <div class="ph" style="left:148px;top:40px;width:82px;height:45px;background:#c9a671" role="img" aria-label="Operator beside vacuum kiln"></div>
  <div class="abs tiny" style="left:138px;top:92px;width:102px;text-align:center;color:#fff">Green timber is loaded into the kiln and automated drying programme for timber species selected.</div>
  <div class="abs tiny" style="left:138px;top:106px;width:102px;text-align:center;color:#fff">Drying takes 6-7 days to dry 50mm timber in a VacuDry Turbo.</div>
  <div class="pill" style="left:160px;top:119px;width:67px;height:9px;line-height:9px;background:var(--lime)">Total time 7 days</div>
</div>

<div class="slide" style="left:260px;top:614px">
  <div class="bar">Post drying process</div>
  <div class="ph" style="left:0;top:18px;width:180px;height:120px;background:linear-gradient(135deg,#6b5d50,#c9b9a0,#8b7b66)" role="img" aria-label="Thicknesser planing timber boards"></div>
  <div class="abs" style="left:130px;top:26px;width:103px;height:104px;border-radius:7px;background:linear-gradient(var(--green),var(--lime))"></div>
  <div class="abs tiny" style="left:140px;top:36px;width:86px;color:#fff;font-size:3.6px">
    <p style="margin-bottom:4px">Dried stair treads are delivered skip dressed or finished to size. We will start with skip dressed product, the simplest to produce.</p>
    <p style="margin-bottom:4px">Skip dressing runs the dried timber through a thicknesser to expose the grain, so each board can be graded Select, Standard or Feature.</p>
    <p>Once dressed, the timber is palletised ready for delivery to the client.</p>
  </div>
</div>

<div class="slide" style="left:513px;top:614px">
  <div class="bar">VacuDry kilns</div>
  <div class="abs tiny" style="left:10px;top:30px;width:102px">
    <p style="margin-bottom:3px">The main advantage is drying in a vacuum, which lowers the boiling point of water.</p>
    <p style="margin-bottom:3px">A lower boiling point needs less energy and reduces stress, checking and warping of the timber.</p>
    <p>The key advantage is drying freshly sawn timber in 7-8 days at 50mm.</p>
  </div>
  <div class="abs tiny" style="left:124px;top:30px;width:110px">
    <p style="color:var(--green);margin-bottom:3px">The drying time is a factor of two things:</p>
    <p>• Vacuum, which draws moisture from the core</p>
    <p style="margin-bottom:3px">• Direct heating plates between each layer</p>
    <p>The result is dried timber with fewer defects and even moisture content, vital for structural integrity.</p>
  </div>
  <div class="abs" style="left:0;top:111px;width:245px;height:27px;background:var(--green)"></div>
  <div class="ph" style="left:26px;top:88px;width:55px;height:38px;background:#4c5a72" role="img" aria-label="Kiln loaded with heating plates"></div>
  <div class="ph" style="left:148px;top:88px;width:55px;height:38px;background:#8c8578" role="img" aria-label="Kiln showing heating plates between layers"></div>
  <div class="abs tiny" style="left:16px;top:131px;color:#fff">Turbo loaded with connected heating plates</div>
  <div class="abs tiny" style="left:132px;top:131px;color:#fff">Turbo showing plates between timber layers</div>
</div>

<!-- Row 4 -->
<div class="slide" style="left:6px;top:760px">
  <div class="bar">About VacuDry</div>
  <div class="ph" style="left:60px;top:30px;width:150px;height:80px;background:radial-gradient(ellipse,#f1f1f1,#fff 70%)" role="img" aria-label="Faint world map"></div>
  <div class="abs small" style="left:21px;top:48px;width:95px;font-size:3.8px">
    <p style="margin-bottom:6px">VacuDry is a Vermont family owned business that has been developing and selling vacuum kiln systems since 1980, with several patents covering modular kilns and controls.</p>
    <p>VacuDry produces over 150 kilns per annum and has a remote service model, selling in the USA, Canada, Mexico, Sweden and New Zealand, with a new office in Europe.</p>
  </div>
  <div class="abs small" style="left:142px;top:48px;width:94px;font-size:3.8px">
    <p style="color:var(--lime);font-weight:700;margin-bottom:3px">Exclusive agreement</p>
    <p style="margin-bottom:3px">On 17 June 2020 Grainline Ventures International entered into an 18 month agreement for the exclusive Australian supply of all VacuDry kilns, subject to two minimum purchase requirements:</p>
    <p style="margin-bottom:2px">• $USXX on or before 17 December 2020; and</p>
    <p>• $USXX on or before 17 December 2021.</p>
  </div>
</div>

<div class="slide" style="left:260px;top:760px">
  <div class="bar">GVI advantages</div>
  <div class="ph" style="left:0;top:18px;width:82px;height:120px;background:linear-gradient(90deg,#3f3522,#6b6640,#2f2a1c)" role="img" aria-label="Tall redwood forest"></div>
  <div class="abs" style="left:72px;top:22px;width:165px">
    <div class="row tiny" style="height:12.8px"><span style="width:13px;color:#fff;font-size:4px">1</span><span><b style="color:var(--green)">Business model is fully self-funding</b> after initial investment</span></div>
    <div class="row tiny" style="height:12.8px"><span style="width:13px;color:#fff;font-size:4px">2</span><span><b style="color:var(--green)">Exclusive access to technology</b> for 18 months in Australia</span></div>
    <div class="row tiny" style="height:12.8px"><span style="width:13px;color:#fff;font-size:4px">3</span><span><b style="color:var(--green)">Less time to dry:</b> vacuum draws moisture from the core</span></div>
    <div class="row tiny" style="height:12.8px"><span style="width:13px;color:#fff;font-size:4px">4</span><span><b style="color:var(--green)">Dry fresh cut timber</b> straight from the sawmill</span></div>
    <div class="row tiny" style="height:12.8px"><span style="width:13px;color:#fff;font-size:4px">5</span><span><b style="color:var(--green)">No timber stock required</b>, so no yard holding cost</span></div>
    <div class="row tiny" style="height:12.8px"><span style="width:13px;color:#fff;font-size:4px">6</span><span><b style="color:var(--green)">Less wastage</b> than conventional drying, around 3%</span></div>
    <div class="row tiny" style="height:12.8px"><span style="width:13px;color:#fff;font-size:4px">7</span><span><b style="color:var(--green)">Higher quality timber</b> with even moisture and colour</span></div>
    <div class="row tiny" style="height:12.8px"><span style="width:13px;color:#fff;font-size:4px">8</span><span><b style="color:var(--green)">Modular design</b> allows easy scaling of production</span></div>
    <div class="row tiny" style="height:12.8px"><span style="width:13px;color:#fff;font-size:4px">9</span><span><b style="color:var(--green)">Specialty timbers</b> such as thick beams dry in weeks</span></div>
  </div>
</div>

<div class="slide" style="left:513px;top:760px">
  <div class="bar">Strategic Plan</div>
  <svg class="abs" style="left:0;top:18px" width="245" height="60" viewBox="0 0 245 60">
    <line x1="0" y1="52" x2="245" y2="52" stroke="var(--lime)" stroke-width="3"/>
    <circle cx="50" cy="31" r="21" fill="none" stroke="var(--green)" stroke-width="4"/>
    <circle cx="126" cy="31" r="21" fill="none" stroke="var(--lime)" stroke-width="4"/>
    <circle cx="200" cy="31" r="21" fill="none" stroke="var(--brown)" stroke-width="4"/>
    <text x="50" y="34" text-anchor="middle" font-family="Signika,sans-serif" font-size="7" font-weight="600" fill="var(--green)">Phase 1</text>
    <text x="126" y="34" text-anchor="middle" font-family="Signika,sans-serif" font-size="7" font-weight="600" fill="var(--lime)">Phase 2</text>
    <text x="200" y="34" text-anchor="middle" font-family="Signika,sans-serif" font-size="7" font-weight="600" fill="var(--brown)">Phase 3</text>
  </svg>
  <ul class="abs tiny" style="left:20px;top:84px;width:70px;list-style:disc">
    <li>Order initial kiln, set up location</li>
    <li>Run test batches of single species</li>
    <li>Sell stair treads to installers</li>
    <li>Expand capacity with more kilns</li>
    <li>Secure supply from private forests</li>
  </ul>
  <ul class="abs tiny" style="left:96px;top:84px;width:72px;list-style:disc">
    <li>Develop client sales network and ordering app</li>
    <li>Expand into high margin niche markets and architectural timbers</li>
  </ul>
  <ul class="abs tiny" style="left:172px;top:84px;width:66px;list-style:disc">
    <li>Establish own sawmilling capacity</li>
  </ul>
</div>

<!-- Row 5 -->
<div class="slide" style="left:6px;top:906px">
  <div class="bar">Business plan</div>
  <div class="abs tiny" style="left:10px;top:26px;width:70px;text-align:center">Rent 300m2 warehouse space near north coast hardwood forests, with an initial three year lease and options to extend.</div>
  <div class="abs tiny" style="left:90px;top:26px;width:68px;text-align:center">To reduce lead time we will order a kiln first and run two production runs before deciding on further kilns.</div>
  <div class="abs tiny" style="left:170px;top:26px;width:68px;text-align:center">After a successful trial we will buy more Turbo units, growing as supply of timber allows.</div>
  <div class="pill" style="left:10px;top:89px;width:70px;height:9px;line-height:9px;background:var(--brown);font-size:4px">Establishment</div>
  <div class="pill" style="left:91px;top:89px;width:65px;height:9px;line-height:9px;background:var(--brown);font-size:4px">VacuDry trial</div>
  <div class="pill" style="left:170px;top:89px;width:68px;height:9px;line-height:9px;background:var(--brown);font-size:4px">Scaling production</div>
  <div class="abs" style="left:0;top:118px;width:245px;height:20px;background:var(--green)"></div>
  <div class="ph" style="left:12px;top:100px;width:56px;height:30px;background:#7b7e7e" role="img" aria-label="Empty warehouse"></div>
  <div class="ph" style="left:94px;top:100px;width:56px;height:30px;background:#4a3a2f" role="img" aria-label="Kiln unit in yard"></div>
  <div class="ph" style="left:176px;top:100px;width:56px;height:30px;background:#b9b3a6" role="img" aria-label="Production hall with kilns"></div>
</div>

<div class="slide" style="left:260px;top:906px">
  <div class="bar">Financials</div>
  <div class="bignum" style="left:14px;top:24px;font-size:14px">1</div>
  <div class="abs tiny" style="left:20px;top:26px;width:76px">GVI will offer investors high returns, with one kiln then two Turbo units by month 7.</div>
  <div class="bignum" style="left:14px;top:46px;font-size:14px">2</div>
  <div class="abs tiny" style="left:20px;top:50px;width:76px">From there we ramp up production in line with sales and kiln capacity.</div>
  <div class="bignum" style="left:14px;top:68px;font-size:14px">3</div>
  <div class="abs tiny" style="left:20px;top:70px;width:76px">We view GVI as a long term hold, paying out most of net profit to investors.</div>
  <div class="bignum" style="left:14px;top:92px;font-size:14px">4</div>
  <div class="abs tiny" style="left:20px;top:96px;width:76px">By year 3 we expect 10 kilns, distributing $XXX per month and retaining $XXX.</div>
  <svg class="abs" style="left:125px;top:22px" width="112" height="46" viewBox="0 0 112 46" role="img" aria-label="Bar chart of four categories">
    <g font-family="Open Sans,sans-serif" font-size="2.6" fill="#555" text-anchor="middle">
      <line x1="4" y1="38" x2="110" y2="38" stroke="#ccc" stroke-width=".4"/>
      <rect x="8" y="12.2" width="4" height="25.8" fill="var(--brown)"/><rect x="13" y="23.6" width="4" height="14.4" fill="var(--lime)"/><rect x="18" y="26" width="4" height="12" fill="#9a9268"/>
      <text x="10" y="11">4.3</text><text x="15" y="22.5">2.4</text><text x="20" y="25">2</text>
      <rect x="35" y="11.6" width="4" height="26.4" fill="var(--brown)"/><rect x="40" y="23" width="4" height="15" fill="var(--lime)"/><rect x="45" y="26" width="4" height="12" fill="#9a9268"/>
      <text x="37" y="10.5">4.4</text><text x="42" y="22">2.5</text><text x="47" y="25">2</text>
      <rect x="62" y="17" width="4" height="21" fill="var(--brown)"/><rect x="67" y="27.2" width="4" height="10.8" fill="var(--lime)"/><rect x="72" y="20" width="4" height="18" fill="#9a9268"/>
      <text x="64" y="16">3.5</text><text x="69" y="26">1.8</text><text x="74" y="19">3</text>
      <rect x="89" y="11" width="4" height="27" fill="var(--brown)"/><rect x="94" y="21.2" width="4" height="16.8" fill="var(--lime)"/><rect x="99" y="8" width="4" height="30" fill="#9a9268"/>
      <text x="91" y="10">4.5</text><text x="96" y="20">2.8</text><text x="101" y="7">5</text>
      <text x="15" y="42">Category 1</text><text x="42" y="42">Category 2</text><text x="69" y="42">Category 3</text><text x="96" y="42">Category 4</text>
    </g>
  </svg>
  <table class="abs" style="left:128px;top:78px;width:108px">
    <tr style="background:var(--brown-dark);color:#fff;font-weight:700"><td style="width:40%"></td><td>Year 1</td><td>Year 2</td><td>Year 3</td></tr>
    <tr style="background:#f3ecd9"><td>EBITDA</td><td></td><td></td><td></td></tr>
    <tr style="background:var(--tan)"><td>Cumulative cash</td><td></td><td></td><td></td></tr>
    <tr style="background:#f3ecd9"><td>No. kilns</td><td></td><td></td><td></td></tr>
    <tr style="background:var(--tan)"><td>Monthly Recurring Profit</td><td></td><td></td><td></td></tr>
  </table>
</div>

<div class="slide" style="left:513px;top:906px">
  <div class="bar">Risk</div>
  <table class="abs" style="left:10px;top:28px;width:225px">
    <tr style="background:var(--brown-dark);color:#fff;text-align:center;font-weight:700"><td style="width:31%;background:var(--brown)">Risk</td><td>Mitigation</td></tr>
    <tr><td style="height:13px">Disruption to log supply</td><td>Coffs Harbour is central to the hardwood forests of the north coast.</td></tr>
    <tr style="background:var(--tan)"><td style="height:13px;background:var(--lime)">Unable to obtain boards from sawmills</td><td>Diversify supply with state and private forests and own milling.</td></tr>
    <tr><td style="height:13px">Timber boards not to specification</td><td>Inspect and grade boards on arrival and reject poor stock.</td></tr>
    <tr style="background:var(--tan)"><td style="height:13px;background:var(--lime)">Kiln doesn't perform to expectations</td><td>Warranty and remote support from the manufacturer apply.</td></tr>
    <tr><td style="height:13px">Ability to supply required species timber</td><td>Start with the most common species and widen the range later.</td></tr>
    <tr style="background:var(--tan)"><td style="height:18px;background:var(--lime)">Copycat competitor</td><td>Our exclusive agreement limits direct competition while we build a loyal client network.</td></tr>
  </table>
</div>

<!-- Row 6 -->
<div class="slide" style="left:130px;top:1052px;height:140px">
  <div class="bar">Risk</div>
  <div class="pill" style="left:8px;top:26px;width:107px;height:9px;line-height:9px;background:var(--lime)">Risk</div>
  <div class="pill" style="left:130px;top:26px;width:107px;height:9px;line-height:9px;background:var(--brown)">Mitigation</div>
  <div class="abs tiny" style="left:40px;top:42px">Competitor response</div>
  <div class="abs tiny" style="left:132px;top:41px;width:104px;text-align:center">In the short term competitors cannot match our drying time or quality. Given the market size we do not expect them to reduce price, and we will build strong client relationships.</div>
  <div class="abs" style="left:0;top:70px;width:245px;height:70px;background:var(--cream)"></div>
  <svg class="abs" style="left:9px;top:76px" width="10" height="60" viewBox="0 0 10 60">
    <g fill="var(--green)"><path d="M5 0 10 8H0Z"/><path d="M5 22 10 30H0Z"/><path d="M5 44 10 52H0Z"/></g>
  </svg>
  <svg class="abs" style="left:128px;top:76px" width="10" height="50" viewBox="0 0 10 50">
    <g fill="var(--green)"><path d="M5 0 10 8H0Z"/><path d="M5 30 10 38H0Z"/></g>
  </svg>
  <div class="abs tiny" style="left:22px;top:74px;width:96px">
    <p style="margin-bottom:3px"><b>Business Model Risk</b><br>Sales timing is the main driver of financial performance.</p>
    <p style="margin-bottom:3px"><b>Strategic Risk</b><br>A specific industry can be affected by events outside our control.</p>
    <p><b>Insolvency Risk</b><br>There is no guarantee the funding will be sufficient.</p>
  </div>
  <div class="abs tiny" style="left:141px;top:74px;width:96px">
    <p style="margin-bottom:4px"><b>Regulatory Risk</b><br>Political, tax or legal change may adversely affect operations and performance.</p>
    <p><b>Liquidity Risk</b><br>Shares are unlisted and there is no open market for them. Investors should seek independent professional advice before investing.</p>
  </div>
</div>

<div class="slide" style="left:383px;top:1052px;height:140px">
  <div class="bar">Our team</div>
  <div class="abs" style="left:12px;top:42px;display:flex;gap:6px">
    <div style="width:52px;height:82px;background:#fff;border:1px solid #eee;position:relative">
      <div style="height:28px;background:var(--green);color:#fff;text-align:center;font-size:4px;padding-top:7px;font-weight:600">YOUR NAME<br>CEO and Director</div>
      <div class="ph" style="left:13px;top:24px;width:25px;height:25px;border-radius:50%;background:#cfc9c2;border:2px solid #fff" role="img" aria-label="Team member portrait"></div>
      <div class="abs tiny" style="left:3px;top:53px;width:46px;text-align:center;font-size:3px">Lorem ipsum dolor sit amet, consectetur adipiscing elit. Donec mauris lorem, vestibulum ac rutrum id, suscipit in dui.</div>
    </div>
    <div style="width:52px;height:82px;background:#fff;border:1px solid #eee;position:relative">
      <div style="height:28px;background:var(--brown);color:#fff;text-align:center;font-size:4px;padding-top:7px;font-weight:600">YOUR NAME<br>CEO and Director</div>
      <div class="ph" style="left:13px;top:24px;width:25px;height:25px;border-radius:50%;background:#cfc9c2;border:2px solid #fff" role="img" aria-label="Team member portrait"></div>
      <div class="abs tiny" style="left:3px;top:53px;width:46px;text-align:center;font-size:3px">Lorem ipsum dolor sit amet, consectetur adipiscing elit. Donec mauris lorem, vestibulum ac rutrum id, suscipit in dui.</div>
    </div>
    <div style="width:52px;height:82px;background:#fff;border:1px solid #eee;position:relative">
      <div style="height:28px;background:var(--green);color:#fff;text-align:center;font-size:4px;padding-top:7px;font-weight:600">YOUR NAME<br>CEO and Director</div>
      <div class="ph" style="left:13px;top:24px;width:25px;height:25px;border-radius:50%;background:#cfc9c2;border:2px solid #fff" role="img" aria-label="Team member portrait"></div>
      <div class="abs tiny" style="left:3px;top:53px;width:46px;text-align:center;font-size:3px">Lorem ipsum dolor sit amet, consectetur adipiscing elit. Donec mauris lorem, vestibulum ac rutrum id, suscipit in dui.</div>
    </div>
    <div style="width:52px;height:82px;background:#fff;border:1px solid #eee;position:relative">
      <div style="height:28px;background:var(--brown);color:#fff;text-align:center;font-size:4px;padding-top:7px;font-weight:600">YOUR NAME<br>CEO and Director</div>
      <div class="ph" style="left:13px;top:24px;width:25px;height:25px;border-radius:50%;background:#cfc9c2;border:2px solid #fff" role="img" aria-label="Team member portrait"></div>
      <div class="abs tiny" style="left:3px;top:53px;width:46px;text-align:center;font-size:3px">Lorem ipsum dolor sit amet, consectetur adipiscing elit. Donec mauris lorem, vestibulum ac rutrum id, suscipit in dui.</div>
    </div>
  </div>
</div>

</body>
</html>
```